Kitchen and cabinets Landing Page design

Hi there
Web Design Task Outline
• Create a Web Design
• Uncoded webpage layout design
• Single Page - Just Homepage Layout
Task Description
* While we need to update our website, we are actually looking at working with a web designer long-term, which will include quite regular design work. So even though this is a small job, we’d love you to respond, as if you do a good job on this one, we would love to continue working with you on a more regular basis.
Please find below all the information for the design of our new website.
The current Web site is www.marrowbank.com.au – don’t laugh!!!
Site Basics:
The site will be the landing page and online home of our kitchen renovation business. We also do vanities, bedroom robes and general cabinetery for the house and office.
Target audience:
? Predominantly home renovation seekers, families (females – decision maker) and builders.
? Most of our business comes from referrals and recommendations, but the site needs to be updated to improve our on line image
General feeling to be conveyed:
Update our old, tired 80’s site (fresh, modern and vital)
Must portray contemporary and up to date attitude - eye-catching / attention grabbing
But not too expensive looking as to alienate people who may think we look too expensive
Landing Page:
Happy to look at your creativity, but must contain a capturing image, contact details (phone), testimonials
Potential Nav Links =
Home
Photo Gallery
Contact Us
Testimonial
Vanities
Entertainment Units
Colours:
Our business has little to do with wood now so the timber look is superseded. We are open to your creative suggestions. We need all marketing media to be consistent and the website can start this process. Our logo is really weak and dated as well. At present we have a green and blue business card with capital QP logo (hmmm), but we’re generally thinking something that represents the home and kitchen
Layout: Open to your creativity
* Samples of Other Good (Similar) Sites We Like:
www.hobplexa.com.au
www.vorny.com.au
www.primacabinetry.com.au/
www.lunafitouts.com.au
www.thejoinerycourt.com.au
Header Text =
Feel free to submit something from your own creative ideas.
Header Image/photo Ideas:
As the site is about kitchen and house hold cabinets, feel free to use an image to reflect that. We are generally thinking to have one main image that is quite eye-catching and attention grabbing. We can supply photos from jobs we have done later.
* Notes:
1. Do not feel completely bound to these ideas. Feel free to convey the basic idea however your creativity desires.
Thanks a lot and look forward to receiving your first design!
Cheers
Gordon
Updates
sorry people - forgot to mention our best selling point!
we were established in 1980, so have been going for 30 years. This is a strong selling point.
We use "30 years of excellence" as a tag.
there are numerous ways of using est. 1980, ie gold label, starburst etc. Go for it.
thanks
Gordon
Hi Designers, My apologies for the delay in responding to your designs. I have been working on other business and have not had a chance to look at them thoroughly. I plan to focus on them today and will provide feedback. Thank you for your understanding.
Reason: Today was the first chance I've had to look at designs. Will be actively providing feedback over next fews day. Am looking to make some changes to the a few of the designs received. Thanks everyone for you patience.

```html
<!DOCTYPE html>
<html lang="en">
<head>
<meta charset="utf-8">
<title>Marrow Bank Cabinets &amp; Furniture</title>
<link rel="stylesheet" href="https://fonts.googleapis.com/css2?family=Arimo:ital,wght@0,400;0,700;1,700&family=Cormorant+Garamond:ital,wght@1,500;1,600&family=Tinos&display=swap">
<style>
:root{
  --timber:#e39b45;
  --timber-dark:#c97a2a;
  --timber-light:#f0b56d;
  --accent:#d8812c;
  --ink:#444;
  --ink-soft:#555;
  --rule:#8a8a8a;
  --frame:#fff;
  --bg-top:#d9d9d9;
  --bg-bottom:#ffffff;
}
*{margin:0;padding:0;box-sizing:border-box}
html,body{width:1164px;height:1200px;overflow:hidden}
body{position:relative;font-family:"Arimo",Arial,sans-serif;color:var(--ink);
  background:linear-gradient(180deg,var(--bg-top) 160px,#ececec 520px,var(--bg-bottom) 760px)}
.site-header{position:absolute;left:0;top:0;width:1164px;height:159px;
  background:linear-gradient(180deg,var(--timber-light),var(--timber) 45%,var(--timber-dark));
  border-bottom:2px solid #f6d7a8;box-shadow:0 3px 6px rgba(0,0,0,.25)}
.brand{position:absolute;left:44px;top:18px;display:flex;align-items:center;gap:10px}
.brand-mark{width:22px;height:22px;border-radius:50%;background:#fff}
.brand-name{font-family:"Tinos",serif;font-size:30px;color:#fff;letter-spacing:1px}
.contact-icon{position:absolute;left:604px;top:18px}
.contact-list{position:absolute;left:689px;top:18px;list-style:none;color:#fff;font-weight:700;
  font-size:16px;line-height:19px;text-shadow:1px 1px 2px rgba(0,0,0,.5)}
.selling-point{position:absolute;right:36px;top:120px;color:#fff;font-weight:700;font-style:italic;
  font-size:19px;text-shadow:1px 1px 2px rgba(0,0,0,.5)}
.intro{position:absolute;left:0;width:1164px;top:182px;text-align:center;
  font-family:"Cormorant Garamond",serif;font-style:italic;font-weight:600;font-size:20px;color:var(--ink-soft)}
.photo{position:absolute;background:var(--frame);border-radius:6px;box-shadow:0 1px 6px rgba(0,0,0,.3);padding:8px}
.photo .fill{width:100%;height:100%}
.photo-bathroom{left:76px;top:250px;width:262px;height:304px}
.photo-bathroom .fill{background:linear-gradient(135deg,#eee7dd,#d8cfc2 60%,#b9a58a)}
.photo-entertainment{left:826px;top:250px;width:260px;height:304px}
.photo-entertainment .fill{background:linear-gradient(180deg,#a79d93,#cfc6bb 55%,#e9e4dd 70%,#9d7352)}
.photo-kitchen{left:318px;top:225px;width:529px;height:354px;z-index:2}
.photo-kitchen .fill{background:linear-gradient(180deg,#d8d3cc,#ece9e4 45%,#f4f2ef 65%,#7a4a30)}
.headline{position:absolute;left:43px;top:638px;width:1078px;height:69px;
  border-top:1px solid var(--rule);border-bottom:1px solid var(--rule);text-align:center;
  font-family:"Cormorant Garamond",serif;font-style:italic;font-weight:500;font-size:44px;line-height:67px;color:var(--ink-soft)}
.column{position:absolute;top:742px;font-size:13px}
.column h2{font-family:"Tinos",serif;font-weight:400;font-size:26px;color:#666;margin-bottom:14px}
.mission{left:39px;width:340px}
.mission h2{color:var(--accent)}
.mission p{margin:0 0 16px 5px;line-height:16.5px;color:var(--ink)}
.testimonials{left:439px;width:300px}
.testimonials blockquote{position:relative;padding-left:31px;line-height:27px;color:var(--ink-soft)}
.testimonials blockquote svg{position:absolute;left:2px;top:8px}
.testimonials cite{font-style:normal;font-weight:700;color:var(--accent)}
.consultation{left:802px;width:330px}
.consultation p{line-height:27px;color:var(--ink-soft)}
a{color:var(--accent)}
.more-link{position:absolute;top:1099px;font-size:12px;color:var(--accent)}
.read-more{left:298px}
.all-testimonials{left:606px}
.site-footer{position:absolute;left:0;top:1147px;width:1164px;height:53px;
  background:linear-gradient(180deg,#f6c98f,var(--timber) 50%,var(--timber-dark));
  border-top:2px solid #bbb;color:#fff;font-size:12px;text-align:center;line-height:51px}
</style>
</head>
<body>
<header class="site-header">
  <div class="brand"><span class="brand-mark"></span><span class="brand-name">Marrow Bank</span></div>
  <svg class="contact-icon" width="66" height="82" viewBox="0 0 66 82" aria-hidden="true">
    <rect x="4" y="2" width="58" height="78" rx="5" fill="#c38a2d" stroke="#7a5416" stroke-width="2"/>
    <rect x="4" y="2" width="12" height="78" rx="4" fill="#8c6120"/>
    <circle cx="39" cy="41" r="16" fill="none" stroke="#fff" stroke-width="4"/>
  </svg>
  <ul class="contact-list">
    <li>Telephone: 039861-444</li>
    <li>Fax: 0398614270</li>
    <li>Address: Factory 5, 418 Kellmore Road, Ashvale Heights</li>
    <li>Email: gordon@marrowbank.com.au</li>
  </ul>
  <p class="selling-point">A strong selling point of ours is "established 1980 / 30 years experience "</p>
</header>

<p class="intro">“ We custom design, build and install quality cabinets, kitchens, bathrooms, laundries, theatre entertainments units, studies and wardrobes.”</p>

<div class="photo photo-bathroom"><div class="fill" role="img" aria-label="Photo of a bright bathroom vanity with flowers"></div></div>
<div class="photo photo-entertainment"><div class="fill" role="img" aria-label="Photo of a white entertainment unit with shelves and a television"></div></div>
<div class="photo photo-kitchen"><div class="fill" role="img" aria-label="Photo of a white kitchen with an island bench and timber floor"></div></div>

<h1 class="headline">Creating Style and Comfort with Cutting-Edge Technology...</h1>

<section class="column mission">
  <h2>OUR MISSION:</h2>
  <p>To produce excellent quality cabinetry<br>every time!</p>
  <p>We cater for those who truly care about quality, workmanship and a high level of personal service. We are proud of ourinnovative designs, superior products, and outstanding service sought after by the discerning customers.</p>
  <p>We custom design, build and install quality cabinets, kitchens, theatre entertainment units, furniture, stone bench tops and stainless steel finishes. Customized work and architectural designs back up with professional advice and personalised service.</p>
  <p><strong>We guarantee all jobs on time and on budget</strong>……</p>
</section>

<section class="column testimonials">
  <h2>TESTIMONIALS:</h2>
  <blockquote>
    <svg width="15" height="15" viewBox="0 0 15 15" aria-hidden="true"><circle cx="7.5" cy="7.5" r="7" fill="#999"/><path d="M6 4.5l3.5 3-3.5 3z" fill="#fff"/></svg>
    "The advice we received from everyone at Marrow Bank was sound, considered and sensitive. We appreciated the staff being here at the time and date arranged and all were a pleasure to deal with. Apart from being extremely competent, we felt they took a distinctly personal interest in the kitchen design and construction, always sensitive to our needs and situation.<br>
    <cite>Tom and Rina Halbrook, Elmcourt</cite> "
  </blockquote>
</section>

<section class="column consultation">
  <h2>CONSULTATION</h2>
  <p>For an obligation FREE Quote and consultation call us on 03 9861 4444 or email <a href="mailto:gordon@marrowbank.com.au">gordon@marrowbank.com.au</a></p>
</section>

<a class="more-link read-more" href="#">READ MORE</a>
<a class="more-link all-testimonials" href="#">ALL TESTIMONIALS</a>

<footer class="site-footer">Marrowbankcabinets&amp;furniture © 2011 . All Rights Reserved</footer>
</body>
</html>
```